Webdesign für Herstellung von Geschenk- und Dekorationsartikeln
Kobalt Prismo ist ein sehr angenehmer und professioneller Designer, der sich viele Gedanken über mein Projekt gemacht hat und ein Design, passend zu meinen Artikeln entworfen hat. Neben einer kompetenten Beratung gab es viele hilfreiche Vorschläge, die über den eigentlichen Auftrag hinaus gingen. Der Designer ist sehr zu empfehlen. Vielen Dank für den freundlichen Kontakt!
Zielgruppe
Wir sind eine kleine Firma, die mit einem Lasergravierer Geschenk- und Dekorationsartikel herstellt, verziert und beschriftet. Hierzu wird hauptsächlich Holz, Papier, Kork, Filz und Glas als Material eingesetzt.
Auch Schmuck , wie z.B. Kettenanhänger und Ohrringe aus Holz werden gefertigt.
Außerdem werden Fotogravur-Arbeiten nach Kundenwunsch angeboten.
Haupt-Zielgruppe sind Frauen ab 30.
Aufgabenstellung
Das Design soll etwas verspielt sein und Freude an den kleinen Dingen des Lebens ausdrücken. Es soll nicht zu sachlich und kühl sein.
Das vorhandene Logo wird bereit gestellt.
Es existiert noch keine Webseite. Die zukünftige Webseite soll über einen Shop verfügen.
Von der Shop-Darstellung her, hat mir die Webseite 'www.qvhauswerk.ch' gefallen.
Es wäre gut, wenn die im Logo vorhandenen Farben auch auf dem Design für die Webseite auftauchen würden.
Als Design-Tool wäre Adobe Photoshop (PSD) für die Erstellung gut.

```html
<!DOCTYPE html>
<html lang="de">
<head>
<meta charset="utf-8">
<title>Lunaria – Personalisierte Lippenstifte</title>
<link href="https://fonts.googleapis.com/css2?family=PT+Sans:wght@400;700&display=swap" rel="stylesheet">
<style>
:root{
  --brown:#b0844a;
  --brown-dark:#a77a3f;
  --cream:#f1e8df;
  --ring:#e9e1d8;
  --white:#ffffff;
  --yellow-a:#ffe14a;
  --yellow-b:#fcc417;
  --track:#e8dccd;
}
*{margin:0;padding:0;box-sizing:border-box}
html,body{width:924px;height:1200px;overflow:hidden;background:var(--white)}
body{font-family:"PT Sans",sans-serif;color:var(--brown);position:relative}
.hero-bg{position:absolute;left:0;top:0}
.abs{position:absolute}
.brand{left:105px;top:52px;font-size:24px;font-weight:400;color:var(--brown);display:flex;align-items:center;gap:6px}
.brand .mark{width:10px;height:10px;border-radius:50%;background:var(--brown)}
.nav{top:66px;font-size:10px;letter-spacing:.3px;display:flex}
.nav a{position:absolute;color:var(--brown);text-decoration:none;white-space:nowrap}
.icons svg{position:absolute;top:66px}
.tag{left:127px;top:178px;border-left:2px solid var(--brown);padding-left:5px;font-size:8.5px;font-weight:700;line-height:10px}
.headline{left:130px;top:262px;font-size:31px;font-weight:700;line-height:37px}
.dot{width:12px;height:12px;border:1px solid var(--brown);border-radius:50%;left:92px}
.dot.active::after{content:"";position:absolute;left:2px;top:2px;width:6px;height:6px;border-radius:50%;background:var(--brown)}
.btn-product{left:133px;top:347px;width:101px;height:25px;border-radius:13px;background:var(--brown);color:var(--white);font-size:9.5px;font-weight:700;display:flex;align-items:center;justify-content:center;box-shadow:2px 2px 0 #d9c9b6}
.hero-ring{left:455px;top:160px;width:286px;height:286px;border-radius:50%;background:var(--ring)}
.hero-photo{left:468px;top:173px;width:260px;height:260px;border-radius:50%;background:radial-gradient(circle at 35% 30%,var(--yellow-a),var(--yellow-b))}
.scroll-track{left:841px;top:280px;width:2px;height:173px;background:var(--track)}
.scroll-thumb{left:839px;top:280px;width:5px;height:32px;background:var(--brown)}
.section-title{left:0;width:938px;top:592px;text-align:center;font-size:15px;font-weight:700}
.section-title span{border-bottom:1px solid #e0cdb6}
.card{top:670px;width:194px}
.card .photo{width:194px;height:194px;background:linear-gradient(160deg,var(--yellow-a),var(--yellow-b))}
.card .info{display:flex;justify-content:space-between;margin-top:7px;font-size:13px}
.card .price{font-weight:700;font-size:12px}
.arrow{top:758px}
.btn-all{left:409px;top:916px;width:123px;height:25px;border:1px solid var(--brown);border-radius:3px;font-size:9.5px;font-weight:700;letter-spacing:.4px;display:flex;align-items:center;justify-content:center}
.footer-brand{left:105px;top:1058px;font-size:20px;display:flex;align-items:center;gap:5px}
.footer-brand .mark{width:8px;height:8px;border-radius:50%;background:var(--brown)}
.f-head{font-size:7px;font-weight:700;top:1050px}
.f-list{font-size:6px;line-height:8px;top:1050px;list-style:none}
.social{top:1063px;display:flex;gap:8px;left:776px}
.social span{width:8px;height:8px;border-radius:50%;background:var(--brown)}
</style>
</head>
<body>
<svg class="hero-bg" width="924" height="1200" viewBox="0 0 924 1200">
  <path d="M0 0H924V722C820 740 700 748 600 744C330 733 120 660 0 522Z" fill="var(--cream)"/>
</svg>

<div class="abs brand"><span class="mark"></span>Lunaria</div>

<nav class="abs nav">
  <a style="left:397px">HOME</a>
  <a style="left:446px">ÜBER UNS</a>
  <a style="left:519px">PRODUKTE</a>
  <a style="left:598px">BLOG</a>
  <a style="left:649px">KONTAKT</a>
</nav>
<div class="icons">
  <svg style="left:752px" width="13" height="13" viewBox="0 0 13 13"><circle cx="5.5" cy="5.5" r="4" fill="none" stroke="var(--brown)" stroke-width="2"/><path d="M8.5 8.5L12 12" stroke="var(--brown)" stroke-width="2.4" stroke-linecap="round"/></svg>
  <svg style="left:778px" width="12" height="13" viewBox="0 0 12 13"><circle cx="6" cy="4" r="3" fill="none" stroke="var(--brown)" stroke-width="1.2"/><path d="M1 12.3V11a3 3 0 0 1 3-3h4a3 3 0 0 1 3 3v1.3Z" fill="none" stroke="var(--brown)" stroke-width="1.2"/></svg>
  <svg style="left:806px" width="14" height="13" viewBox="0 0 14 13"><path d="M0.5 1H2.5L4 9H12L13 3.5H3" fill="none" stroke="var(--brown)" stroke-width="1.3" stroke-linejoin="round"/><circle cx="5" cy="11.5" r="1" fill="var(--brown)"/><circle cx="11" cy="11.5" r="1" fill="var(--brown)"/></svg>
</div>

<div class="abs tag">Sommer Kollektion<br>Lippenstifte</div>
<h1 class="abs headline">Personalisierte<br>Lippenstifte</h1>
<div class="abs dot active" style="top:289px"></div>
<div class="abs dot" style="top:312px"></div>
<div class="abs dot" style="top:335px"></div>
<div class="abs btn-product">zum Produkt</div>

<div class="abs hero-ring"></div>
<div class="abs hero-photo" role="img" aria-label="Foto eines gelben Lippenstifts auf gelbem Grund"></div>
<div class="abs scroll-track"></div>
<div class="abs scroll-thumb"></div>

<h2 class="abs section-title"><span>Neu im Sortiment</span></h2>

<svg class="abs arrow" style="left:76px" width="16" height="16" viewBox="0 0 16 16"><path d="M14 8H3M8 3L3 8L8 13" fill="none" stroke="var(--brown)" stroke-width="2.2" stroke-linecap="round" stroke-linejoin="round"/></svg>
<div class="abs card" style="left:150px"><div class="photo" role="img" aria-label="Foto eines gelben Lippenstifts"></div><div class="info"><span>Lippenstift (gelb)</span><span class="price">3.33€</span></div></div>
<div class="abs card" style="left:374px"><div class="photo" role="img" aria-label="Foto eines gelben Lippenstifts"></div><div class="info"><span>Lippenstift (gelb)</span><span class="price">3.33€</span></div></div>
<div class="abs card" style="left:598px"><div class="photo" role="img" aria-label="Foto eines gelben Lippenstifts"></div><div class="info"><span>Lippenstift (gelb)</span><span class="price">3.33€</span></div></div>
<svg class="abs arrow" style="left:830px" width="16" height="16" viewBox="0 0 16 16"><path d="M2 8H13M8 3L13 8L8 13" fill="none" stroke="var(--brown)" stroke-width="2.2" stroke-linecap="round" stroke-linejoin="round"/></svg>

<div class="abs btn-all">ALLE ANZEIGEN</div>

<footer>
  <div class="abs footer-brand"><span class="mark"></span>Lunaria</div>
  <div class="abs f-head" style="left:267px">SITEMAP</div>
  <ul class="abs f-list" style="left:312px"><li>Kontakt</li><li>Über Uns</li><li>Verpackung &amp; Versand</li><li>FAQ</li><li>Rücksendungen</li><li>Produkte</li></ul>
  <div class="abs f-head" style="left:420px">INFORMATIONEN</div>
  <ul class="abs f-list" style="left:495px"><li>AGB</li><li>Datenschutz</li><li>Impressum</li></ul>
  <div class="abs social"><span></span><span></span><span></span></div>
</footer>
</body>
</html>
```